Laminated Training Card; highly professional yet engaging, colorful, fits branding

We need an 8 1/2" x 11" piece, printed front and back, to inspire and offer instructions for nonprofit leaders on key coaching skills to use with their staff. Though it's in a professional services setting, this piece communicates a sense of fun and excitement to encourage leaders to try out these skills, and keep the training card close at hand. An infographic style would be ideal.

Target Market(s)

Nonprofit leaders will use the laminated training card in a face to face training class, and then take it back to the office to use to 'train' their staff

Industry/Entity Type

Training

Font styles to use
Serif

Requirements
Must have
• See project brief attached
Nice to have
Should not have

```html
<!DOCTYPE html>
<html lang="en">
<head>
<meta charset="utf-8">
<title>Accountability Culture – Training Card</title>
<link href="https://fonts.googleapis.com/css2?family=Raleway:wght@500;600;700;800&family=Roboto:wght@400;500;700&display=swap" rel="stylesheet">
<style>
  :root {
    --sky: #b2def0;
    --sky-light: #e6f4fa;
    --green: #b7c934;
    --fold: #3a3d40;
    --ink: #2b2b2b;
    --orange: #e2582a;
    --orange-dark: #c9461d;
    --brand-grey: #6d6e71;
    --footer: #343434;
    --white: #ffffff;
  }
  * { box-sizing: border-box; margin: 0; padding: 0; }
  html, body { width: 848px; height: 1200px; overflow: hidden; }
  body {
    position: relative;
    background: linear-gradient(to bottom, var(--white) 0, var(--sky-light) 100px, var(--sky) 230px);
    font-family: "Roboto", Arial, sans-serif;
    color: var(--ink);
  }

  .brand {
    position: absolute; top: 22px; left: 0; width: 848px;
    display: flex; justify-content: center; align-items: center; gap: 16px;
  }
  .brand-dot { width: 70px; height: 70px; border-radius: 50%; background: var(--brand-grey); }
  .brand-name {
    font-family: "Raleway", Arial, sans-serif; font-weight: 700;
    font-size: 31px; line-height: 1.15; color: var(--brand-grey);
  }

  .headline {
    position: absolute; top: 150px; left: 0; width: 848px; text-align: center;
    font-family: "Raleway", Arial, sans-serif; font-weight: 600;
    font-size: 21.5px; line-height: 32px; letter-spacing: 0.4px; color: var(--ink);
  }
  .headline .accent { color: var(--orange); font-weight: 800; }

  .figure-area {
    position: absolute; left: 550px; top: 300px; width: 270px; height: 623px;
    border-radius: 120px 120px 0 0;
    background: linear-gradient(to bottom, #d3dde3 0%, #c3ccd2 55%, #8a7470 100%);
  }

  .section-banner {
    position: absolute; left: 0; width: 541px; height: 56px;
    background: var(--green);
    font-family: "Raleway", Arial, sans-serif; font-weight: 800;
    font-size: 27px; line-height: 56px; padding-left: 36px; color: var(--ink);
  }
  .section-banner .fold { position: absolute; right: -21px; top: -14px; }
  .banner-questions { top: 246px; }
  .banner-leadership { top: 610px; }

  .section-body {
    position: absolute; left: 31px; width: 500px;
    font-size: 16.3px; line-height: 21.5px;
  }
  .section-body p { margin-bottom: 21.5px; }
  .body-questions { top: 326px; }
  .body-leadership { top: 684px; }

  .results-band {
    position: absolute; left: 0; top: 923px; width: 848px; height: 195px;
    background: var(--orange);
  }
  .swirl-area {
    position: absolute; left: 18px; top: 885px; width: 150px; height: 110px;
    border-radius: 55px; background: var(--orange-dark);
  }
  .results {
    position: absolute; left: 80px; top: 966px; width: 700px; text-align: center;
  }
  .results h2 {
    font-weight: 500; font-size: 18.5px; letter-spacing: 0.5px; color: var(--ink);
    margin-bottom: 6px;
  }
  .results ul { list-style: none; }
  .results li {
    font-weight: 700; font-size: 19px; line-height: 29.5px; letter-spacing: 0.4px;
    color: var(--white);
  }

  .footer {
    position: absolute; left: 0; top: 1118px; width: 848px; height: 82px;
    background: var(--footer); color: var(--white);
    display: flex; justify-content: space-between; align-items: center;
    padding: 0 20px 0 29px; font-size: 16px;
  }
</style>
</head>
<body>
  <header class="brand">
    <div class="brand-dot"></div>
    <div class="brand-name">Steadfast Center<br>for Nonprofit Leadership</div>
  </header>

  <h1 class="headline">CREATE AN ACCOUNTABILITY CULTURE WITH<br>TEAMS AND ALLIES <span class="accent">VALUABLE TIPS FOR SUCCESS</span></h1>

  <div class="figure-area" role="img" aria-label="Illustration of a smiling businessman in glasses and tie, finger raised, leaning beside a brown briefcase"></div>

  <div class="section-banner banner-questions">POWERFUL QUESTIONS
    <svg class="fold" width="22" height="14" viewBox="0 0 22 14"><polygon points="0,0 22,14 0,14" fill="var(--fold)"/></svg>
  </div>
  <div class="section-body body-questions">
    <p>Coach yourself asking powerful questions; they break your internal monologue. Ask others a powerful question — that you don't answer.&nbsp; They will feel deeply heard.</p>
    <p>Dream one moment: What's possible? And establish accountability the next: What should I do when you miss your deadline?</p>
    <p>Asking questions isn't reserved for the leader. Whoever asks the powerful questions is the leader in the moment.</p>
    <p>With whom is it safe to ask powerful questions in your culture?</p>
  </div>

  <div class="section-banner banner-leadership">4 DIMENSIONS OF LEADERSHIP
    <svg class="fold" width="22" height="14" viewBox="0 0 22 14"><polygon points="0,0 22,14 0,14" fill="var(--fold)"/></svg>
  </div>
  <div class="section-body body-leadership">
    <p>Knowing when to move between these stances = leadership mastery.</p>
    <p>Leading from the front: eyes on the vision and staying connected to those who follow Leading from the side:&nbsp; locking arms in the company of equals. Eyes on the shared vision, but each has their own path to get there.</p>
    <p>Leading from behind: ‘fading’ while still holding the space. You've got their backs. Leading from above: seeing the big picture</p>
  </div>

  <div class="results-band"></div>
  <div class="swirl-area" role="img" aria-label="Decorative orange swirl ornament"></div>
  <section class="results">
    <h2>ACCOUNTABILITY CULTURES SRESULTS</h2>
    <ul>
      <li>-&nbsp; Improve productivity&nbsp; Speed decision making</li>
      <li>-&nbsp; Reduce stress and compassion fatigue</li>
      <li>-&nbsp; Have more fun and fulfillment</li>
      <li>-&nbsp; Build trust</li>
    </ul>
  </section>

  <footer class="footer">
    <span>www.steadfastcenter.org</span>
    <span>info@steadfastcenter.org</span>
  </footer>
</body>
</html>
```